Mobile Recording Studio needs business cards

Open to seeing a creative design, but I want to emphasis my logo and minimize the name/title and company information. Possible a fully black background on card.

My company is a mobile sound recording studio. ok to include a my trailer (actual or cartoon) on the card. My initial thought is more straight forward, but a good design will win me over.

SPECS:
CMYK color mode
High (300ppi) raster effect.
cover bleed area
please deliver: Illustrator file with layers and a pdf at completion.

Name and info for the business card:

Dallin Perry
ADR Mixer

email: Dallin@MixVault.com

address:
248 - 5170 East Hollister
Vancouver, BC V5R 2J4

phone:
604.518.2093 office

website:
www.MixVault.com

FB: @MixVault

Instagram: @TheMixVault

Industry/Entity Type

Television Production

Contact Information for Business Card

Dallin Perry
ADR Mixer

email: Dallin@MixVault.com

address:
248 - 5170 East Hollister
Vancouver, BC V5R 2J4

phone:
604.518.2093 office

website:
www.MixVault.com

FB: @MixVault

Instagram: @TheMixVault

Colors

Designer to choose colors to be used in the design.

Requirements
Must have
• emphasis my logo and minimize the name/title and company information.
• SPECS:
• CMYK color mode
• High (300ppi) raster effect.
• cover bleed area
• please deliver: Illustrator file with layers and a pdf at completion.
Nice to have
• maybe include the following:
• all black background or black theme
• my work trailer (actual or cartoon) refer to Instagram: @TheMixVault

```html
<!DOCTYPE html>
<html lang="en">
<head>
<meta charset="utf-8">
<title>MixVault Business Card</title>
<link href="https://fonts.googleapis.com/css2?family=Libre+Baskerville:wght@700&family=Arimo:wght@400;700&display=swap" rel="stylesheet">
<style>
  :root {
    --backdrop: #2a2a2a;
    --card: #050505;
    --silver: #cfcfcf;
    --silver-dark: #9a9a9a;
    --white: #f2f2f2;
  }
  * { margin: 0; padding: 0; box-sizing: border-box; }
  html, body { width: 1200px; height: 900px; overflow: hidden; background: var(--backdrop); }
  .stage { position: relative; width: 1200px; height: 900px; }
  .card {
    position: absolute; left: 240px; width: 720px; height: 411px;
    background: var(--card); overflow: hidden;
  }
  .card--front { top: 30px; }
  .card--back { top: 459px; }

  .brand {
    position: absolute; left: 0; right: 0; top: 0; bottom: 0;
    display: flex; flex-direction: column; align-items: center; justify-content: center;
  }
  .brand__name {
    font-family: "Libre Baskerville", serif; font-weight: 700;
    font-size: 96px; letter-spacing: 2px; color: var(--silver); line-height: 1;
  }
  .brand__rule { width: 440px; height: 4px; background: var(--silver); margin-top: 22px; }

  .contact {
    position: absolute; left: 52px; top: 64px; color: var(--white);
    font-family: "Arimo", sans-serif;
  }
  .contact__name {
    font-family: "Libre Baskerville", serif; font-weight: 700;
    font-size: 20px; letter-spacing: 2px; margin-left: 52px;
  }
  .contact__title { font-size: 13px; letter-spacing: 1px; margin-left: 52px; margin-top: 4px; }
  .contact__address { font-size: 13px; font-weight: 700; letter-spacing: 1px; line-height: 1.55; margin-left: 40px; margin-top: 26px; }
  .contact__list { list-style: none; margin-top: 14px; margin-left: 20px; }
  .contact__item { display: flex; align-items: center; gap: 10px; font-size: 13px; font-weight: 700; letter-spacing: 1px; height: 24px; }
  .contact__item svg { width: 18px; height: 18px; flex: none; }
  .social { display: flex; gap: 56px; margin-top: 20px; font-size: 14px; letter-spacing: 1px; }
  .social__item { display: flex; align-items: center; gap: 8px; }
  .social__mark { width: 18px; height: 18px; border: 2px solid var(--white); border-radius: 4px; }

  .trailer-photo { position: absolute; left: 0; top: 0; width: 720px; height: 411px; }
</style>
</head>
<body>
<div class="stage">
  <section class="card card--front">
    <div class="brand">
      <div class="brand__name">MixVault</div>
      <div class="brand__rule"></div>
    </div>
  </section>

  <section class="card card--back">
    <svg class="trailer-photo" viewBox="0 0 720 411" role="img" aria-label="Photo of the black mobile recording studio trailer parked outdoors">
      <defs>
        <linearGradient id="trailerTones" x1="0" y1="0" x2="0" y2="1">
          <stop offset="0" stop-color="#8a8576"/>
          <stop offset="0.25" stop-color="#2e2e30"/>
          <stop offset="0.8" stop-color="#1c1c1e"/>
          <stop offset="1" stop-color="#6b6353"/>
        </linearGradient>
      </defs>
      <path d="M470 82 H720 V411 H440 Q330 250 470 82 Z" fill="url(#trailerTones)"/>
    </svg>

    <div class="contact">
      <div class="contact__name">DALLIN PERRY</div>
      <div class="contact__title">ADR Mixer</div>
      <div class="contact__address">248 - 5170 East Hollister<br>Vancouver, BC V5R 2J4</div>
      <ul class="contact__list">
        <li class="contact__item">
          <svg viewBox="0 0 18 18" fill="none" stroke="currentColor" stroke-width="1.5"><rect x="5" y="1.5" width="8" height="15" rx="1.5"/><line x1="8" y1="14" x2="10" y2="14"/></svg>
          604.518.2093
        </li>
        <li class="contact__item">
          <svg viewBox="0 0 18 18" fill="none" stroke="currentColor" stroke-width="1.5"><rect x="1.5" y="4" width="15" height="10"/><path d="M1.5 4 L9 10 L16.5 4"/></svg>
          Dallin@MixVault.com
        </li>
        <li class="contact__item">
          <svg viewBox="0 0 18 18" fill="none" stroke="currentColor" stroke-width="1.3"><circle cx="9" cy="9" r="7.5"/><ellipse cx="9" cy="9" rx="3.5" ry="7.5"/><line x1="1.5" y1="9" x2="16.5" y2="9"/><line x1="3" y1="5" x2="15" y2="5"/><line x1="3" y1="13" x2="15" y2="13"/></svg>
          www.MixVault.com
        </li>
      </ul>
      <div class="social">
        <span class="social__item"><span class="social__mark"></span>TheMixVault</span>
        <span class="social__item"><span class="social__mark"></span>MixVault</span>
      </div>
    </div>
  </section>
</div>
</body>
</html>
```